Please look at my website to get a better understanding of my business: www.perovatu.com
This business is about Life Coaching for Families, couples, teenagers and individuals. I work more w parents of teenagers (as well as teenagers) but not so much with young kids.
The card should be fun, not too busy, with a sense of flow and playfulness. Warm colors, artistic style (can have a family sculpture, paining or a picture in it). Basic information about myself and my company

Reason: I extended my due date for next Tuesday, November 13th. Please summit new designs if you haven't done so, and for those who submitted, thank you so much for your time and effort. I will make a decision next Tues, and will contact you if I need to revise some items. Much thanks to you all! Orla

Families, parents, teenagers, couples, individuals.

Business

• Business name: PeRoVaTu! Hearth Circle Life Coaching
My name: Orla Bekwith, RMTQ
Description of my work: Tri-Mode life coach
Tel: 555-304-7719
Website: www.PeRoVaTu.com
• Family sculpture, abstract painting or a picture, or simply a nice background w/out a picture added.
• Corporate feeling, cold colors, corporate symbols. no Sunset, or picture of families on the beach.
Don't include bar-code (from uploaded file 1, it is only the designer to find out more about my website).

```html
<!DOCTYPE html>
<html lang="en">
<head>
<meta charset="utf-8">
<title>PeRoVaTu Business Card</title>
<link rel="stylesheet" href="https://fonts.googleapis.com/css2?family=Exo+2:wght@300;400&display=swap">
<style>
  :root {
    --page-bg: #e9eaea;
    --card-red: #b83222;
    --band-orange: #b95a26;
    --band-gold: #d39c40;
    --text-gold: #d9a23f;
    --text-white: #ffffff;
    --text-red: #c8261e;
  }
  html, body {
    margin: 0;
    padding: 0;
    width: 1200px;
    height: 900px;
    overflow: hidden;
    background: var(--page-bg);
  }
  .canvas {
    position: relative;
    width: 1200px;
    height: 900px;
    display: flex;
    align-items: center;
    justify-content: center;
  }
  .business-card {
    display: block;
    width: 960px;
    height: 537px;
    font-family: "Exo 2", sans-serif;
  }
  .card-base { fill: var(--card-red); }
  .band-orange { fill: var(--band-orange); }
  .band-gold { fill: var(--band-gold); }
  .company-name, .company-tagline { fill: var(--text-gold); font-weight: 400; font-size: 16.5px; }
  .person-name { fill: var(--text-white); font-weight: 400; font-size: 22px; }
  .person-credential { font-size: 16.5px; }
  .person-role { fill: var(--text-white); font-weight: 400; font-size: 18px; }
  .contact-phone { fill: var(--text-gold); font-weight: 300; font-size: 17px; }
  .contact-web { fill: var(--text-red); font-weight: 400; font-size: 17px; }
</style>
</head>
<body>
<main class="canvas">
  <svg class="business-card" viewBox="0 0 531 297" xmlns="http://www.w3.org/2000/svg" aria-label="PeRoVaTu business card">
    <rect class="card-base" x="0" y="0" width="531" height="297"/>
    <polygon class="band-orange" points="413,0 531,0 531,297 294,297"/>
    <polygon class="band-gold" points="531,24 531,297 421,297"/>

    <g class="company">
      <text class="company-name" x="67" y="71">PeRoVaTu</text>
      <text class="company-tagline" x="67" y="94">Hearth Circle Life Coaching</text>
    </g>

    <g class="person">
      <text class="person-name" x="67" y="220">Orla Bekwith, <tspan class="person-credential">RMTQ</tspan></text>
      <text class="person-role" x="67" y="244">Tri-Mode life coach</text>
    </g>

    <g class="contact">
      <text class="contact-phone" transform="translate(409 276) rotate(-68)">Tel: 555-304-7719</text>
      <text class="contact-web" transform="translate(452 274) rotate(-68)">www.perovatu.com</text>
    </g>
  </svg>
</main>
</body>
</html>
```